Classic Minimalistic Business Card

Design a classic, minimalistic Business Card. Please find inspiration in the attached Classic Minimalistic examples. My information:
Name: Glen Ovamir
Company: Ovamir Capital
Logo: OC
Address: 1470 N Thornwick Rd, Suite 210 | Larkmoor, OH 44210
Phone: 555-555-0192
Email: glenovamir@pvt.insure
Slogan: Building Strength Through Capital

Feel free to leave out any of the information above except my name.

I have selected Double-sided, but I am also open to Single-sided

Target Market(s)

22-70. income greater than 150k/year

Industry/Entity Type

Finance

Contact Information for Business Card

See Project Description

Requirements
Must have
• Ivory or "antiqued" background similar to the reference pictures

```html
<!DOCTYPE html>
<html lang="en">
<head>
<meta charset="utf-8">
<title>Ovamir Capital — Business Card</title>
<link rel="stylesheet" href="https://fonts.googleapis.com/css2?family=Special+Elite&display=swap">
<style>
  :root {
    --backdrop: #d8d8d8;
    --ivory-light: #f6f3e6;
    --ivory-mid: #f1e6c6;
    --ivory-edge: #e6cf94;
    --ink-navy: #1f1d38;
    --ink-gold: #c99a34;
    --card-shadow: rgba(0, 0, 0, 0.18);
  }
  * { margin: 0; padding: 0; box-sizing: border-box; }
  html, body {
    width: 1200px;
    height: 846px;
    overflow: hidden;
    background: var(--backdrop);
  }
  .canvas {
    position: relative;
    width: 1200px;
    height: 846px;
    display: flex;
    align-items: center;
    justify-content: center;
    gap: 60px;
  }
  .card {
    position: relative;
    width: 500px;
    height: 340px;
    border-radius: 3px;
    background:
      radial-gradient(ellipse at 50% 50%, var(--ivory-light) 0%, var(--ivory-light) 35%, var(--ivory-mid) 70%, var(--ivory-edge) 100%);
    box-shadow: 0 10px 24px var(--card-shadow);
    font-family: "Special Elite", "Courier New", monospace;
    font-weight: 400;
    overflow: hidden;
  }
  /* front */
  .brand {
    position: absolute;
    top: 46px;
    left: 0;
    right: 0;
    display: flex;
    align-items: center;
    justify-content: center;
    gap: 10px;
    color: var(--ink-navy);
    font-size: 22px;
    letter-spacing: 1px;
  }
  .brand-dot {
    width: 22px;
    height: 22px;
    border-radius: 50%;
    background: var(--ink-gold);
  }
  .holder {
    position: absolute;
    left: 44px;
    top: 150px;
    color: var(--ink-navy);
  }
  .holder-name {
    font-size: 26px;
    font-weight: 400;
    letter-spacing: 1px;
    margin-bottom: 16px;
  }
  .holder-contact {
    font-size: 14px;
    line-height: 1.45;
  }
  .office-address {
    position: absolute;
    left: 44px;
    bottom: 40px;
    color: var(--ink-navy);
    font-size: 13px;
    letter-spacing: 0.3px;
    white-space: nowrap;
  }
  /* back */
  .card-back {
    display: flex;
    flex-direction: column;
    align-items: center;
    justify-content: center;
    gap: 22px;
  }
  .back-brand {
    display: flex;
    align-items: center;
    gap: 12px;
    color: var(--ink-gold);
    font-size: 30px;
    letter-spacing: 1px;
  }
  .back-brand .brand-dot {
    width: 30px;
    height: 30px;
  }
  .tagline {
    color: var(--ink-gold);
    font-size: 15px;
    letter-spacing: 0.5px;
  }
</style>
</head>
<body>
  <main class="canvas">
    <section class="card card-front" aria-label="Business card front">
      <div class="brand">
        <span class="brand-dot"></span>
        <span class="brand-name">Ovamir Capital</span>
      </div>
      <div class="holder">
        <h1 class="holder-name">Glen Ovamir</h1>
        <p class="holder-contact">555-555-0192<br>glenovamir@pvt.insure</p>
      </div>
      <p class="office-address">1470 N Thornwick Rd, Suite 210 | Larkmoor, OH 44210</p>
    </section>

    <section class="card card-back" aria-label="Business card back">
      <div class="back-brand">
        <span class="brand-dot"></span>
        <span class="brand-name">Ovamir Capital</span>
      </div>
      <p class="tagline">Building Strength Through Capital</p>
    </section>
  </main>
</body>
</html>
```